Bed Company needs business card

Hello, we are a bed company that makes specialized magnets for beds. We are an alternative healing company. I need a modern and upscale business card. Please incorporate my logo for the card.

Accepted file formats are AI, EPS, and Press-Ready PDFS.

Please include all fonts or convert them to outlines regardless of file type.

If you are designing the card in Photoshop the file Must be 1200dpi.

I am open to anything for the business card.  I really like all of your designs and if you want to change the color of the logo, you can.  I will be making the final selection by Friday.  Thank You for all of your designs.  Feel Free to submit different color logos if you want.  

Reason: I will make a decision Final on Friday April 20th. 2012. Good Luck and Thank you all for the designs.

Target Market(s)

My target Market is people, who are looking for alternative healing.

Industry/Entity Type

Business

Requirements
Must have
• My logo must be incorporated. The front card must have

Name
Job Title

Address
Work
Cell
Fax
email
web

Just put in fake info for the card.

The back of the card. I want the logo on the back with color. I just want it to look modern and cool.

```html
<!DOCTYPE html>
<html lang="en">
<head>
<meta charset="utf-8">
<title>Lodestone Rest — Business Card</title>
<link rel="stylesheet" href="https://fonts.googleapis.com/css2?family=Open+Sans:wght@400;700&display=swap">
<style>
  :root {
    --stage: #3b3b3d;
    --leaf: #52b848;
    --forest: #1f6b2a;
    --paper: #ffffff;
  }
  html, body {
    margin: 0;
    padding: 0;
    width: 1200px;
    height: 1000px;
    overflow: hidden;
    background: var(--stage);
    font-family: "Open Sans", Arial, sans-serif;
  }
  .canvas {
    position: relative;
    width: 1200px;
    height: 1000px;
  }
  .card {
    position: absolute;
    width: 762px;
    height: 465px;
    border-radius: 9px;
    overflow: hidden;
  }
  .card--back {
    left: 63px;
    top: 15px;
    background: var(--leaf);
  }
  .card--front {
    left: 400px;
    top: 509px;
    background: var(--paper);
  }
  .card__panel {
    position: absolute;
    left: 0;
    top: 0;
    width: 417px;
    height: 100%;
    background: var(--leaf);
  }

  /* brand lockup */
  .brand {
    position: absolute;
    display: flex;
    align-items: center;
    gap: 16px;
  }
  .brand__mark {
    width: 40px;
    height: 40px;
    background: var(--forest);
    flex: none;
  }
  .brand__text { display: flex; flex-direction: column; }
  .brand__name {
    font-weight: 700;
    line-height: 1;
    white-space: nowrap;
  }
  .brand__tagline {
    font-weight: 400;
    letter-spacing: 1px;
    margin-top: 6px;
    white-space: nowrap;
  }
  .card--back .brand { left: 148px; top: 180px; }
  .card--back .brand__mark { width: 64px; height: 64px; }
  .card--back .brand__name { font-size: 58px; color: var(--paper); }
  .card--back .brand__tagline { font-size: 20px; color: var(--forest); align-self: flex-end; }

  .card--front .brand { left: 460px; top: 180px; gap: 12px; }
  .card--front .brand__name { font-size: 36px; color: var(--leaf); }
  .card--front .brand__tagline { font-size: 15px; color: var(--leaf); align-self: flex-end; }

  .card__web {
    position: absolute;
    left: 0;
    right: 0;
    top: 418px;
    text-align: center;
    font-size: 19px;
    letter-spacing: 5px;
    color: var(--forest);
  }

  /* contact details */
  .person {
    position: absolute;
    left: 40px;
    top: 52px;
  }
  .person__name {
    margin: 0;
    font-size: 43px;
    font-weight: 400;
    line-height: 1.1;
    color: var(--paper);
  }
  .person__title {
    margin: 2px 0 0;
    font-size: 16px;
    color: var(--forest);
  }
  .contact {
    position: absolute;
    left: 40px;
    margin: 0;
    padding: 0;
    list-style: none;
    font-size: 17px;
    line-height: 28px;
  }
  .contact--phone { top: 161px; }
  .contact--reach { top: 280px; }
  .contact__row { display: flex; }
  .contact__label { color: var(--forest); margin-right: 6px; }
  .contact__value { color: var(--paper); }
</style>
</head>
<body>
<main class="canvas">
  <section class="card card--back" aria-label="Card back">
    <div class="brand">
      <span class="brand__mark"></span>
      <div class="brand__text">
        <span class="brand__name">Lodestone Rest</span>
        <span class="brand__tagline">Alternative Healing</span>
      </div>
    </div>
    <p class="card__web">www.lodestonerest.example</p>
  </section>

  <section class="card card--front" aria-label="Card front">
    <div class="card__panel"></div>
    <div class="person">
      <h1 class="person__name">Name</h1>
      <p class="person__title">Job title</p>
    </div>
    <ul class="contact contact--phone">
      <li class="contact__row"><span class="contact__label">Mob:</span><span class="contact__value">0400 000 118</span></li>
      <li class="contact__row"><span class="contact__label">Fax:</span><span class="contact__value">0400 000 118</span></li>
    </ul>
    <ul class="contact contact--reach">
      <li class="contact__row"><span class="contact__label">Web:</span><span class="contact__value">www.lodestonerest.example</span></li>
      <li class="contact__row"><span class="contact__label">Email:</span><span class="contact__value">hello@lodestonerest.example</span></li>
      <li class="contact__row"><span class="contact__label">Address:</span><span class="contact__value">18 Harbour Lane<br>Kelmore , ST 40012</span></li>
    </ul>
    <div class="brand">
      <div class="brand__text">
        <span class="brand__name">Lodestone Rest</span>
        <span class="brand__tagline">Alternative Healing</span>
      </div>
    </div>
  </section>
</main>
</body>
</html>
```